PSD for an Italian pizza restaurant web site.

I need an PSD for a Italian pizza restaurant web site.
I have all the php coding work done I just need the front end layout.
I have attached the logo.
Colors to be used
Black
Green
Red
White
Must have navigation buttons across header under logo and left column.
No other requirements!!
Anything Goes!!
Thoughts or ideals:
Fading colors
Textured back ground.
maybe old paper look
Italian flag
The restaurant food includes
pizza, pasta, salads and sandwiches
The restaurant is not a fast food restaurant.
Its a finer dining restaurant.
The current website is extremely bad.
http://www.brunellotrattoria.com/

```html
<!DOCTYPE html>
<html lang="en">
<head>
<meta charset="utf-8">
<title>Brunello's Italian Restaurant</title>
<link href="https://fonts.googleapis.com/css2?family=Cinzel:wght@400;700&family=Crimson+Pro:ital,wght@0,400;0,700;1,700&display=swap" rel="stylesheet">
<style>
:root{
  --red:#c8121b;
  --red-dark:#8e0a10;
  --green:#1f7a1f;
  --green-dark:#0f4f12;
  --black:#111;
  --white:#fff;
  --paper:#efe3c4;
  --paper-edge:#d9c69a;
  --footer:#1c1c1c;
}
*{margin:0;padding:0;box-sizing:border-box}
html,body{width:1200px;height:773px;overflow:hidden}
body{position:relative;font-family:"Crimson Pro",serif;color:var(--white);background:#2a2a2a}
.backdrop{position:absolute;inset:0;background:radial-gradient(ellipse at 20% 70%,#c8452b 0%,#7a2a14 35%,transparent 60%),radial-gradient(ellipse at 85% 45%,#e7b050 0%,#9b5a22 30%,transparent 55%),linear-gradient(180deg,#1a1d1b 0%,#3a2a1e 45%,#a85a2e 100%)}
.abs{position:absolute}
.brand{left:324px;top:24px;width:190px;height:63px;background:var(--black);display:flex;align-items:center;justify-content:center;padding:0 8px}
.brand-name{font:700 14px/1.15 "Cinzel",serif;color:var(--white);text-align:center;letter-spacing:.5px}
.rule{left:324px;top:89px;width:603px;height:3px;background:var(--red-dark)}
.hero{left:324px;top:92px;width:473px;height:229px;background:radial-gradient(ellipse at 65% 40%,#e9c39c 0%,#b8743e 30%,#3a1a0c 70%),#1a0d08}
.badge{left:658px;top:200px;width:98px;height:98px;border-radius:50%;background:var(--black);border:3px solid var(--white);display:flex;align-items:center;justify-content:center;text-align:center;font:700 italic 19px/1 "Crimson Pro",serif;transform:rotate(-18deg)}
.dots{left:576px;top:309px;width:56px;height:13px;background:rgba(0,0,0,.7);border-radius:7px;display:flex;gap:6px;align-items:center;justify-content:center}
.dots i{width:6px;height:6px;border-radius:50%;background:var(--white)}
.dots i.on{background:var(--red)}
.nav{left:797px;top:92px;width:130px;height:229px;background:linear-gradient(180deg,var(--green) 0%,var(--green-dark) 100%);padding-top:16px}
.nav ul{list-style:none}
.nav li{font:700 13px/21px "Cinzel",serif;padding-left:17px;letter-spacing:.5px}
.nav li.current{background:var(--black)}
.nav-phone{position:absolute;left:9px;top:168px;font:400 17px "Crimson Pro",serif}
.offer{left:324px;top:324px;width:603px;height:120px;background:radial-gradient(ellipse at 50% 50%,var(--paper) 40%,var(--paper-edge) 100%);border-radius:4px}
.offer-head{position:absolute;left:10px;top:10px;display:flex;align-items:flex-end;gap:2px}
.offer h2{font:700 16px "Cinzel",serif;color:var(--black)}
.thumbs{position:absolute;left:9px;top:37px;display:flex;gap:6px}
.thumb{width:67px;display:flex;flex-direction:column;align-items:center}
.thumb .pic{width:67px;height:46px;border:2px solid #6b5a3a}
.thumb span{margin-top:8px;font:400 9px "Cinzel",serif;color:var(--black);white-space:nowrap}
.more{position:absolute;right:12px;top:104px;background:var(--green);border-radius:6px;font:700 9px "Cinzel",serif;padding:2px 8px;border:1px solid var(--white)}
.welcome{left:324px;top:444px;width:409px;height:277px;background:radial-gradient(ellipse at 40% 40%,#e3262c 0%,var(--red) 45%,var(--red-dark) 100%)}
.welcome-pic{left:12px;top:11px;width:160px;height:97px;border:3px solid var(--white);background:linear-gradient(135deg,#e9b28a,#7a3a24)}
.welcome h1{left:180px;top:10px;font:700 italic 22px "Crimson Pro",serif;letter-spacing:1px}
.intro{left:180px;top:34px;width:224px;font:400 10px/13.7px "Crimson Pro",serif;text-transform:uppercase}
.pizza-name{left:0;width:409px;top:122px;text-align:center;font:700 italic 27px/1 "Crimson Pro",serif;letter-spacing:.5px}
.info{left:10px;top:159px;font:400 11px/13px "Crimson Pro",serif;text-transform:uppercase}
.info .motto{font-style:italic;font-size:13px}
.info .phone{font-size:21px;line-height:24px;margin-top:6px}
.hours{left:236px;top:159px;font:400 10.5px/13.5px "Crimson Pro",serif;text-transform:uppercase}
.order{left:233px;top:231px;width:131px;height:28px;background:linear-gradient(180deg,#3fa03a,var(--green-dark));border:2px solid var(--white);border-radius:5px;text-align:center;font:700 17px/24px "Cinzel",serif}
.side{left:733px;width:194px}
.specials{top:451px;height:57px;background:linear-gradient(90deg,var(--green),var(--green-dark))}
.coupons{top:512px;height:57px;background:var(--black)}
.promo h3{position:absolute;left:10px;top:7px;font:700 italic 17px "Crimson Pro",serif;letter-spacing:.5px}
.promo p{position:absolute;left:14px;top:28px;font:700 italic 10px "Crimson Pro",serif}
.promo .click{position:absolute;left:108px;top:30px;background:var(--red);border-radius:5px;font:700 9px "Cinzel",serif;padding:2px 6px}
.party{top:576px;height:131px;background:var(--black);border:2px solid var(--white)}
.party-pic{position:absolute;left:0;top:0;width:190px;height:80px;background:radial-gradient(ellipse at 50% 30%,#ffcc55 0%,#e04020 40%,#2a0808 85%)}
.party p{position:absolute;left:8px;top:84px;font:400 9px "Crimson Pro",serif}
.party strong{position:absolute;left:8px;top:96px;font:700 13px/14px "Crimson Pro",serif;width:110px}
.party .learn{position:absolute;left:124px;top:109px;background:var(--red);border-radius:5px;font:700 8px "Cinzel",serif;padding:2px 5px}
.footer{left:324px;top:721px;width:603px;height:38px;background:var(--footer);display:flex;align-items:center;padding-left:11px;font:700 7.5px "Cinzel",serif;white-space:nowrap}
.footer a{color:var(--white);text-decoration:none}
.footer a.current{color:var(--red)}
.footer .sep{margin:0 8px}
.footer .copy{margin-left:auto;margin-right:12px;font-weight:400;font-size:7px}
</style>
</head>
<body>
<div class="backdrop" role="img" aria-label="Close-up photograph of a cheesy pizza with peppers and salami being lifted by a server"></div>

<header class="abs brand">
  <span class="brand-name">BRUNELLO'S<br>ITALIAN RESTAURANT</span>
</header>
<div class="abs rule"></div>

<div class="abs hero" role="img" aria-label="Photograph of a smiling woman holding a pepperoni pizza slice"></div>
<div class="abs badge">Special<br>Offer!</div>
<div class="abs dots"><i></i><i></i><i class="on"></i><i></i></div>

<nav class="abs nav">
  <ul>
    <li class="current">Home</li>
    <li>Sandwiches</li>
    <li>Specialities</li>
    <li>Appetizers</li>
    <li>Beverages</li>
    <li>Lunch Menu</li>
  </ul>
  <div class="nav-phone">(555) 210-3344</div>
</nav>

<section class="abs offer">
  <div class="offer-head">
    <h2>WHAT WE OFFER</h2>
    <svg width="20" height="18" viewBox="0 0 22 20"><path d="M2 18 C2 6 10 1 21 1 C20 12 13 18 2 18Z" fill="#5aa02c"/></svg>
  </div>
  <div class="thumbs">
    <div class="thumb"><div class="pic" role="img" aria-label="Italian pizza photo" style="background:#9b4a2a"></div><span>ITALIAN PIZZA</span></div>
    <div class="thumb"><div class="pic" role="img" aria-label="Italian pizza photo" style="background:#b8642e"></div><span>ITALIAN PIZZA</span></div>
    <div class="thumb"><div class="pic" role="img" aria-label="Burger photo" style="background:#7a5a34"></div><span>BURGER</span></div>
    <div class="thumb"><div class="pic" role="img" aria-label="Sandwiches photo" style="background:#c89a4a"></div><span>SANDWICHES</span></div>
    <div class="thumb"><div class="pic" role="img" aria-label="Pizza photo" style="background:#a85a34"></div><span>PIZZA</span></div>
    <div class="thumb"><div class="pic" role="img" aria-label="Salad photo" style="background:#6a7a34"></div><span>SALADS</span></div>
    <div class="thumb"><div class="pic" role="img" aria-label="Pizza photo" style="background:#b84a24"></div><span>PIZZA</span></div>
    <div class="thumb"><div class="pic" role="img" aria-label="Salad photo" style="background:#5a8a3a"></div><span>SALADS</span></div>
  </div>
  <span class="more">MORE</span>
</section>

<section class="abs welcome">
  <div class="abs welcome-pic" role="img" aria-label="Photograph of three friends sharing pizza"></div>
  <h1 class="abs">WELCOME</h1>
  <p class="abs intro">We believe our pizza is the very best! Our dough is made fresh daily, we buy the highest quality cheese and toppings, our vegetables are fresh and never frozen. This is why we believe our pizza is the very best.</p>
  <div class="abs pizza-name">BRUNELLO'S PIZZA</div>
  <div class="abs info">
    <div class="motto">" We Top All Pizzas"</div>
    <div>Dine In ~ Carry Out ~ Delivery</div>
    <div style="font-size:8.5px">Delivery Times: 11 AM ~ 2 PM and 5 PM ~ Close</div>
    <div class="phone">210-3344</div>
    <div>1820 Elm Hollow Road</div>
    <div style="margin-top:4px">(In Millbrook)</div>
  </div>
  <div class="abs hours">
    <div>Sunday - Closed</div>
    <div>Monday - 11 A.M. - 10 P.M.</div>
    <div>Tues., Wed., Thur. - 11 A.M. - 9 P.M.</div>
    <div>Friday - 11 A.M. - 10 P.M.</div>
    <div>Saturday - 4 P.M. - 10 P.M.</div>
  </div>
  <div class="abs order">ORDER NOW</div>
</section>

<aside class="abs side promo specials"><h3>DAILY SPECIALS</h3><p>CALL FOR DETAILS</p><span class="click">CLICK HERE</span></aside>
<aside class="abs side promo coupons"><h3>COUPONS</h3><p>CALL FOR DETAILS</p><span class="click">CLICK HERE</span></aside>
<aside class="abs side party">
  <div class="party-pic" role="img" aria-label="Party crowd under bright stage lights"></div>
  <p>You're Havin' A Party...</p>
  <strong>We've Got A Free Party Room!</strong>
  <span class="learn">LEARN MORE</span>
</aside>

<footer class="abs footer">
  <a class="current">HOME</a><span class="sep">|</span>
  <a>SANDWICHES</a><span class="sep">|</span>
  <a>SPECIALITIES</a><span class="sep">|</span>
  <a>APPETIZERS</a><span class="sep">|</span>
  <a>BEVERAGES</a><span class="sep">|</span>
  <a>LUNCH MENU</a>
  <span class="copy">© 2013 WWW.BRUNELLOTRATTORIA.COM</span>
</footer>
</body>
</html>
```